Quorvex - Automated robotic Inspection with AI need new business cards

We need a new design of our business cards. The company is focused on automated quality control at high speed with unmatched results. We have a logo but need a more forward leaning business card that shows that we are delivering cutting edge technology.

Contact Information for Business Card

Name
Position
Adress
Phone
Email
e.g.
Lena Holmqvist
Chief Financial Officer (CFO)

Quorvex Sweden AB
Bruksvägen 14, SE-175 43 JÄRFÄLLA, Sweden
Mobile: +46735 21 47 83 | Office: +46 8 61 94 27
www.quorvex-example.com

Font styles to use
Sans Serif

```html
<!DOCTYPE html>
<html lang="en">
<head>
<meta charset="utf-8">
<title>Quorvex Business Cards</title>
<link rel="stylesheet" href="https://fonts.googleapis.com/css2?family=Asap:wght@400;500;600&display=swap">
<style>
  :root {
    --stage: #e9e7e3;
    --card-light: #f7f7f7;
    --card-dark: #273b46;
    --brand-blue: #2a5f8c;
    --ink-light: #ffffff;
    --ink-soft: #e6e4e6;
    --shadow: rgba(0, 0, 0, 0.18);
  }
  * { box-sizing: border-box; margin: 0; padding: 0; }
  html, body {
    width: 1200px;
    height: 900px;
    overflow: hidden;
    background: var(--stage);
    font-family: "Asap", Arial, sans-serif;
  }
  .stage {
    width: 1200px;
    height: 900px;
    display: flex;
    flex-direction: column;
    align-items: center;
    justify-content: center;
    gap: 36px;
  }
  .card {
    position: relative;
    width: 700px;
    height: 400px;
    box-shadow: 0 8px 24px var(--shadow);
    overflow: hidden;
  }
  /* Front face */
  .card--front { background: var(--card-light); }
  .front-brand {
    position: absolute;
    left: 0; right: 0; top: 130px;
    display: flex;
    align-items: center;
    justify-content: center;
    gap: 22px;
  }
  .brand-dot {
    width: 54px; height: 54px;
    border-radius: 50%;
    background: var(--brand-blue);
  }
  .front-brand .brand-name {
    font-size: 84px;
    font-weight: 500;
    color: var(--brand-blue);
    letter-spacing: 3px;
    line-height: 1;
  }
  .front-web {
    position: absolute;
    right: 30px; bottom: 26px;
    font-size: 22px;
    color: var(--brand-blue);
    letter-spacing: 1px;
  }
  /* Back face */
  .card--back { background: var(--card-dark); color: var(--ink-light); }
  .back-brand {
    position: absolute;
    left: 250px; top: 46px;
    display: flex;
    align-items: center;
    gap: 18px;
  }
  .back-brand .brand-dot { width: 44px; height: 44px; background: var(--ink-soft); }
  .back-brand .brand-name {
    font-size: 68px;
    font-weight: 500;
    color: var(--ink-soft);
    letter-spacing: 3px;
    line-height: 1;
  }
  .person {
    position: absolute;
    left: 78px; top: 172px;
  }
  .person-name { font-size: 24px; font-weight: 600; letter-spacing: 0.5px; }
  .person-role { font-size: 16px; margin-top: 2px; }
  .contact {
    position: absolute;
    left: 340px; top: 248px;
    list-style: none;
    font-size: 15px;
    line-height: 1.3;
  }
  .contact-row {
    display: flex;
    align-items: flex-start;
    gap: 22px;
    margin-bottom: 12px;
  }
  .contact-icon { width: 26px; height: 26px; flex: none; }
  .contact-text { padding-top: 4px; }
</style>
</head>
<body>
<main class="stage">
  <section class="card card--front" aria-label="Card front">
    <div class="front-brand">
      <span class="brand-dot"></span>
      <span class="brand-name">Quorvex</span>
    </div>
    <p class="front-web">www.quorvex-example.com</p>
  </section>

  <section class="card card--back" aria-label="Card back">
    <div class="back-brand">
      <span class="brand-dot"></span>
      <span class="brand-name">Quorvex</span>
    </div>
    <div class="person">
      <p class="person-name">Lena Holmqvist</p>
      <p class="person-role">Chief Financial Officer (CFO)</p>
    </div>
    <ul class="contact">
      <li class="contact-row">
        <svg class="contact-icon" viewBox="0 0 24 24" aria-hidden="true">
          <circle cx="12" cy="12" r="11" fill="#fff"/>
          <path d="M12 5.5a4 4 0 0 0-4 4c0 3 4 8 4 8s4-5 4-8a4 4 0 0 0-4-4z" fill="#273b46"/>
          <circle cx="12" cy="9.5" r="1.5" fill="#fff"/>
        </svg>
        <span class="contact-text">Quorvex Sweden AB<br>Bruksvägen 14, SE-175 43 JÄRFÄLLA, Sweden</span>
      </li>
      <li class="contact-row">
        <svg class="contact-icon" viewBox="0 0 24 24" aria-hidden="true">
          <path d="M6.6 3.5l2.6 3.4-1.5 2c1 2.2 2.9 4.2 5.2 5.3l2-1.5 3.5 2.5-1.2 3c-6.6.2-12.6-6.2-12-12.5z" fill="#fff"/>
        </svg>
        <span class="contact-text">+46735 21 47 83 | Office: +46 8 61 94 27</span>
      </li>
      <li class="contact-row">
        <svg class="contact-icon" viewBox="0 0 24 24" aria-hidden="true" fill="none" stroke="#fff" stroke-width="1.4">
          <circle cx="12" cy="12" r="10"/>
          <ellipse cx="12" cy="12" rx="4.5" ry="10"/>
          <path d="M2 12h20M4 7h16M4 17h16"/>
        </svg>
        <span class="contact-text">www.quorvex-example.com</span>
      </li>
    </ul>
  </section>
</main>
</body>
</html>
```